Flyer Personenführungsanlage
Zielgruppe
Unser Unternehmen bietet Kommunikationslösungen rund um Veranstaltungen, Events und Messen an. Für Vorführungen auf Messen, Werksführungen und Dolmetscheraufgaben bieten wir sogenannte "Personenführungsanlagen" zur Miete an. Diese Anlagen bestehen aus einem Handmikrofon oder einem Headset, die Zuhörer erhalten einen Taschenempfänger mit Ohrhörer. Unsere Zielgruppe sind Eventagenturen, Veranstaltungstechnikfirmen, Kirchen, Schwerhörige, sowie Cityguides und Veranstalter.
Aufgabenstellung
Wir möchten für die Personenführungsanlage einen eigenen Produktflyer (max. 4 Seiten) im DIN lang Format 10,5cm x 21,0 cm entwickeln lassen. Alle Informationen und Texte zu diesen Produkten sind auf unserer Webseite. Der Flyer soll die auf der Einführungseite den Anwendungszweck von Personenführungsanlagen erklären, im Anschluss die Produkte Handsender KV-5, Taschenempfänger ZL-3, Ohrhörer MF-4,Kopfhörer MF-6, Induktionsschleife WE-700 sowie den Koffer B72 darstellen, und am Schluss die Einsatzgebiete des Systems (Besichtigungen,Dolmetschertechnik,Hörunterstützung,Effektives Training und Live Kommentare).

```html
<!DOCTYPE html>
<html lang="de">
<head>
<meta charset="utf-8">
<title>Flyer Personenführungsanlage</title>
<link href="https://fonts.googleapis.com/css2?family=Open+Sans:wght@400;600;700&family=Roboto+Condensed:wght@700&display=swap" rel="stylesheet">
<style>
:root{
  --teal:#1787a3;
  --ink:#1f1f1f;
  --grey:#c9c9c9;
  --grey-dark:#5a5a5a;
  --paper:#ffffff;
  --bg:#e6e6e4;
}
*{box-sizing:border-box;margin:0;padding:0}
html,body{width:1200px;height:742px;overflow:hidden;background:var(--bg)}
body{position:relative;font-family:"Open Sans",sans-serif;color:var(--ink)}
.head{font-family:"Roboto Condensed",sans-serif;font-weight:700}
.panel{position:absolute;top:70px;height:530px;background:var(--paper);box-shadow:0 2px 6px rgba(0,0,0,.25);overflow:hidden}

/* cover */
.cover{left:44px;width:262px}
.cover .edge{position:absolute;left:0;top:0;width:6px;height:160px;background:var(--teal)}
.brand{position:absolute;top:46px;left:0;right:0;text-align:center}
.brand-name{font-family:"Open Sans",sans-serif;font-weight:700;font-size:30px;letter-spacing:1px;color:var(--teal);display:inline-flex;align-items:center;gap:8px}
.brand-name i{display:inline-block;width:8px;height:8px;border-radius:50%;background:var(--teal)}
.cover-photo{position:absolute;top:155px;left:6px;right:0;height:160px;background:linear-gradient(120deg,#c9cdd2,#8e8a84 55%,#3d3d40)}
.cover-band{position:absolute;top:315px;left:6px;right:0;bottom:0;background:var(--teal)}
.cover-title{position:absolute;top:338px;left:26px;color:#fff;font-size:21px}

/* Einsatzgebiete */
.uses{left:328px;width:265px;display:flex;flex-direction:column}
.uses-head{background:var(--teal);color:#fff;font-size:13px;padding:8px 12px;height:30px;flex:none}
.uses-body{padding:4px 8px 0 0;flex:1;overflow:hidden}
.uses h3{background:var(--ink);color:#fff;font-size:7.8px;padding:4px 12px;border-radius:0 6px 6px 0;margin:7px 0 5px}
.uses p{color:var(--teal);font-size:6.2px;line-height:1.42;margin:0 0 4px 12px;text-align:justify}
.uses p.strong{font-weight:700}
.uses-foot{flex:none;height:28px;background:#e3e3e3;font-size:6.5px;font-weight:700;text-align:right;padding:11px 10px 0}

/* spread */
.spread{left:620px;width:528px;background:var(--grey)}
.blk{position:absolute}
.bar{background:var(--teal);color:#fff;font-size:13px;padding:7px 24px}
.intro{left:0;top:30px;width:264px;height:186px;background:#fff;padding:10px 14px 0 24px}
.intro p{font-size:6px;line-height:1.38;text-align:justify;margin-bottom:7px}
.card{padding:6px 8px;font-size:5.4px;line-height:1.42;text-align:justify;border-radius:14px;overflow:hidden}
.card h4{font-size:8px;margin-bottom:4px}
.card.teal{background:var(--teal);color:#fff}
.card.white{background:#fff}
.card.black{background:var(--ink);color:#fff}
.card.dark{background:var(--grey-dark);color:#fff}
.card.white h4{color:var(--teal)}
.right h4{text-align:right}
.shot{border-radius:12px;background:#fff}
.shot span{display:block;width:100%;height:100%;border-radius:12px}
</style>
</head>
<body>

<section class="panel cover">
  <div class="edge"></div>
  <div class="brand">
    <div class="brand-name"><i></i>VANDORA</div>
  </div>
  <div class="cover-photo" role="img" aria-label="Foto: Sprecher mit Handmikrofon und Zuhörer mit Ohrhörern"></div>
  <div class="cover-band"></div>
  <h1 class="cover-title head">Personenführungsanlage</h1>
</section>

<section class="panel uses">
  <h2 class="uses-head head">Einsatzgebiete</h2>
  <div class="uses-body">
    <h3 class="head">Führungen / Besichtigungen</h3>
    <p>Durch persönliche Führungen wird die Besichtigung zum individuellen Erlebnis für Ihre Gäste. Mit der Besucherführungsanlage Vocaro können mehrere Gruppen gleichzeitig unabhängig voneinander an Führungen teilnehmen. Jeder Besucher kann seine Lautstärke individuell einstellen. Bei Besuchern mit Hörgeräten kann der Ton durch eine Induktionsschleife direkt auf das eigene Hörgerät übertragen werden.</p>
    <h3 class="head">Dolmetschersystem und mobile Flüsteranlage</h3>
    <p>Als Dolmetschersystem wird Vocaro für zwei Anwendungsbereiche eingesetzt:</p>
    <p>Im Zusammenhang mit Dolmetschertechnik dient Vocaro zur drahtlosen Übertragung der Fremdsprachen an die Konferenzteilnehmer. Die Teilnehmer wählen einfach den Kanal für ihre Sprache aus.</p>
    <p>Beim Flüsterdolmetschen wird Vocaro als mobile Flüsteranlage eingesetzt. Hierbei bietet die individuell einstellbare Stummschaltung des Handsenders optimale Arbeitsbedingungen für Dolmetscher.</p>
    <h3 class="head">Schwerhörigenanlage zur Hörunterstützung in öffentlichen Einrichtungen</h3>
    <p>Barrierefreies Hören in Schulen, Kirchen, Kinos, Theatern oder Stadien leicht gemacht: Mit dem Vocaro Drahtlossystem zur Hörunterstützung wird der Beitrag akustisch verstärkt.</p>
    <p>Anstelle des Hörers können auch Induktionsschleifen für Hörgeräte mit Induktionsspulen eingesetzt werden. Mit Vocaro als Schwerhörigenanlage werden Sie bei Veranstaltungen immer jedes Wort verstehen.</p>
    <h3 class="head">Kommandoanlage für effektives Training</h3>
    <p>Überall wo Trainingsinhalte übermittelt werden sollen, ist Vocaro Ihr optimaler Begleiter:</p>
    <p>Ob beim Pferdesport, beim Rudersport, am Hundeübungsplatz, am Verkehrsübungsplatz oder bei Unterweisungen an großen und lauten Maschinen – mit Vocaro als Kommandoanlage werden die Anweisungen des Trainers und Experten auch über weitere Entfernungen verstanden und die Übungen können optimal umgesetzt werden.</p>
    <h3 class="head">Übertragungssystem für Live Kommentare für Sehbehinderte</h3>
    <p class="strong">Sorgen Sie für Gleichberechtigung und schließen Sie keine Fans aus.</p>
    <p class="strong">Durch spezielle Live-Kommentare können Sehbehinderte z.B. bei Sportveranstaltungen dem Geschehen folgen und dabei an der Stimmung im Stadion unmittelbar teilhaben.</p>
    <p class="strong">Mit dem drahtlosen Übertragungssystem Vocaro werden die Kommentare sicher und mit optimaler Sprachverständlichkeit an die Besucher übertragen.</p>
  </div>
  <div class="uses-foot">www.vandora-rent.de</div>
</section>

<section class="panel spread">
  <h2 class="blk bar head" style="left:0;top:0;width:264px;height:30px">Führungsanlage</h2>
  <div class="blk intro">
    <p>Das gesprochene Wort ist bei der Übertragung von Informationen unerlässlich: Ob im kleinen Personenkreis oder innerhalb großer Gruppen. Egal ob bei Werks- oder Stadtführungen, Bus- oder Schiffsreisen, Dolmetscher- bzw. Hörunterstützung oder Trainings - die optimale Verständigung mit Ihren Gästen ist unerlässlich.</p>
    <p>Bei diesen Anforderungen werden zur Unterstützung sogenannte Führungsanlagen oder auch Flüsteranlagen eingesetzt.</p>
    <p>Es gibt zahlreiche Systeme von unterschiedlichsten Herstellern am Markt. Eines der modernsten Systeme auch in Punkto Zuverlässigkeit, Robustheit und Einfachheit in der Bedienung ist das Tour Guide System Vocaro aus dem Hause Klangwerk.</p>
    <p>Wir vermieten das Klangwerk Vocaro System - das grosse Spektrum der Anwendungsmöglichkeiten sowie die breite Auswahl an Zubehör haben uns von diesem System überzeugt.</p>
  </div>
  <h2 class="blk bar head" style="left:0;top:222px;width:264px;height:32px">Produkte</h2>
  <div class="blk head" style="right:12px;top:8px;color:#fff;font-size:13px">Produkte</div>

  <div class="blk shot" style="left:6px;top:270px;width:67px;height:112px"><span role="img" aria-label="Produktfoto Taschenempfänger ZL-3" style="background:radial-gradient(circle,#9a9da2,#fff 70%)"></span></div>
  <div class="blk card white right" style="left:79px;top:272px;width:183px;height:113px">
    <h4 class="head">Taschenempfänger ZL-3</h4>
    Der leichte Empfänger kann bequem am Gürtel befestigt oder mit einer Trageschlaufe um den Hals getragen werden - die Reichweite beträgt ca. 100m bei Sichtverbindung. Wie bei den Sendern können bis 18 unterschiedliche Frequenzen ausgewählt werden. Die Lautstärke wird über einen Drehregler eingestellt. Als Kopfhörer stehen unterschiedliche Ohrhörer zur Auswahl. Alle Funktionen können über eine Sperrfunktion gegen versehentliches Verstellen gesperrt werden. Die Versorgung erfolgt über 2 AA-Akkus.
  </div>
  <div class="blk card teal" style="left:0;top:393px;width:189px;height:118px;border-radius:0 14px 14px 0">
    <h4 class="head">Handsender KV-5</h4>
    Der <b>Handsender KV-5</b> kann mit beliebig vielen Taschenempfängern ZL-3 eingesetzt werden. Die Reichweite des Handsenders beträgt ca. 100m bei Sichtverbindung. Der Sender bietet bis zu 18 unterschiedliche Frequenzen. Die Sendetaste unterhalb der Mikrofonkopfes kann vom Nutzer individuell als Schalter, Taster oder Mute-Funktion eingestellt werden. Das geräuschkompensierte Mikrofon verfügt über eine rückkopplungsarme Nierencharakteristik. Die Stromversorgung erfolgt über 2 handelsübliche AA-Batterien bzw. Akkus.
  </div>
  <div class="blk shot" style="left:195px;top:395px;width:67px;height:116px"><span role="img" aria-label="Produktfoto Handsender KV-5" style="background:radial-gradient(circle,#7d8288,#fff 70%)"></span></div>

  <div class="blk shot" style="left:266px;top:33px;width:74px;height:117px"><span role="img" aria-label="Produktfoto Ohrhörer MF-4" style="background:radial-gradient(circle,#6e6e6e,#fff 65%)"></span></div>
  <div class="blk card teal right" style="left:348px;top:33px;width:180px;height:113px;border-radius:14px 0 0 14px">
    <h4 class="head">Ohrhörer MF-4</h4>
    Der <b>Ohrhörer MF-4</b> wird zusammen mit dem <b>Taschenempfänger ZL-3</b> zum Einsatz. Für optimalen Tragekomfort sorgt der dehnbare Ohrbügel. Das für den Hörer verwendete Neodym-Magnetsystem sorgt für hervorragende Klangeigenschaften und beste Sprachverständlichkeit. Der Ohrhörer kann wahlweise links oder rechts getragen werden. Die Oberfläche des Ohrhörers kann leicht gereinigt werden und ist somit hygienisch einwandfrei für den nächsten Einsatz.
  </div>
  <div class="blk card white" style="left:266px;top:152px;width:162px;height:104px">
    <h4 class="head">Kopfhörer MF-6</h4>
    Alternativ zum Ohrhörer kann der <b>Kopfhörer MF-6</b> eingesetzt werden. Der zweiseitige Kopfbügelhörer kann seitlich individuell auf den Kopf des Trägers eingestellt werden. Das Kabel zum Taschenempfänger ZL-3 hat eine Länge von 80cm. Die Schaumstoffüberzüge der Ohrhörer können nach Gebrauch leicht ausgetauscht werden und sorgen für maximale Hygiene.
  </div>
  <div class="blk shot" style="left:437px;top:152px;width:89px;height:100px"><span role="img" aria-label="Produktfoto Kopfhörer MF-6" style="background:radial-gradient(circle,#555,#fff 65%)"></span></div>
  <div class="blk shot" style="left:266px;top:268px;width:84px;height:116px"><span role="img" aria-label="Produktfoto Induktionsschleife WE-700" style="background:radial-gradient(circle,#9a9a9a,#fff 65%)"></span></div>
  <div class="blk card black right" style="left:356px;top:265px;width:172px;height:120px;border-radius:14px 0 0 14px">
    <h4 class="head">Induktionsschleife WE-700</h4>
    Mit der <b>Induktionsschleife WE-700</b> können Menschen mit Induktions-Hörgeräten ganz einfach eingebunden werden. Einfach die Induktionsschleife an den Taschenempfänger ZL-3 anschliessen, die Schleife um den Hals hängen und die Veranstaltung kann beginnen. Die Induktionsschleife wird von allen gängigen Induktions-Hörgeräten (z.B. AUDIVO) unterstützt.
  </div>
  <div class="blk card dark" style="left:266px;top:395px;width:141px;height:116px">
    <h4 class="head">Lade-und Transportkoffer</h4>
    Die Vocaro Führungsanlage liefern wir ab 10 Taschenempfänger im praktischen <b>Lade- und Transportkoffer</b>. Das integrierte Ladegerät bietet Platz für bis zu 20 Taschenempfängern sowie einem Handsender. Die seitlichen Fächer nehmen bis zu 40 Headsets bzw. Induktionsschleifen auf. Der Trolley im Reisekofferformat ist mit Rollen ausgestattet und kann bequem an den Einsatzort transportiert werden.
  </div>
  <div class="blk shot" style="left:413px;top:395px;width:113px;height:116px"><span role="img" aria-label="Produktfoto Lade- und Transportkoffer B72 mit Zubehör" style="background:radial-gradient(circle,#a5a8ac,#fff 70%)"></span></div>
</section>

</body>
</html>
```